Electrical construction, completion and commissioning
Keystone Ridge Services
Use same font as used in my logo
not sure may try a few options
Professional
Callum Brody
Director
PO Box 7819 East Perth WA 6892
callum@keystoneridgeservices.com.au
keystoneridgeservices.com.au
EC 20735
ABN 48 271 502 936
Electrical Construction Engineering Completions Commissioning Management and Supervision

```html
<!DOCTYPE html>
<html lang="en">
<head>
<meta charset="utf-8">
<title>Keystone Ridge Services — Stationery</title>
<link href="https://fonts.googleapis.com/css2?family=Exo+2:wght@700&family=Open+Sans:wght@400;600&display=swap" rel="stylesheet">
<style>
  :root{
    --bg:#eeeff1;
    --paper:#ffffff;
    --blue:#2f80d1;
    --blue-deep:#1f64b3;
    --red:#d6322c;
    --ink:#5b6570;
    --faint:#e9eef4;
    --shadow:0 2px 6px rgba(0,0,0,.12);
  }
  *{margin:0;padding:0;box-sizing:border-box}
  html,body{width:1200px;height:936px;overflow:hidden;background:var(--bg)}
  .canvas{position:relative;width:1200px;height:936px}
  .sheet{position:absolute;background:var(--paper);box-shadow:var(--shadow);overflow:hidden}
  .sheet svg.swoosh{position:absolute;inset:0;width:100%;height:100%}
  .brand{position:absolute;display:flex;align-items:center;gap:8px;white-space:nowrap}
  .brand-dot{border-radius:50%;background:var(--red);flex:none}
  .brand-name{font-family:"Exo 2",sans-serif;font-weight:700;color:var(--blue);letter-spacing:.02em;line-height:1}
  .small{font-family:"Open Sans",sans-serif;color:var(--ink);line-height:1.45}

  .letterhead{left:182px;top:68px;width:390px;height:540px}
  .letterhead .brand{left:26px;top:40px}
  .letterhead .brand-dot{width:20px;height:20px}
  .letterhead .brand-name{font-size:11px}
  .letterhead .contact{position:absolute;left:262px;top:30px;font-size:5.5px}
  .letterhead .mark-faint{position:absolute;left:140px;top:205px;width:110px;height:110px;border-radius:50%;background:var(--faint)}

  .folder{left:633px;top:38px;width:460px;height:578px}
  .folder .brand{left:0;right:0;top:232px;flex-direction:column;gap:14px}
  .folder .brand-dot{width:58px;height:58px}
  .folder .brand-name{font-size:25px}

  .card{left:40px;width:203px;border-radius:4px}
  .card-front{top:658px;height:91px}
  .card-front .brand{left:10px;top:14px;gap:4px}
  .card-front .brand-dot{width:10px;height:10px}
  .card-front .brand-name{font-size:6px}
  .card-front .details{position:absolute;left:14px;top:34px;font-size:4.5px}
  .card-back{top:772px;height:108px;background:var(--blue)}
  .card-back .brand{left:0;right:0;top:30px;flex-direction:column;gap:6px}
  .card-back .brand-dot{width:26px;height:26px}
  .card-back .brand-name{font-size:8px;color:#fff}
  .card-back .web{position:absolute;left:0;right:0;bottom:12px;text-align:center;font-size:4.5px;color:#e6f0fb}

  .envelope-front{left:266px;top:672px;width:422px;height:203px}
  .envelope-front .brand{left:20px;top:20px}
  .envelope-front .brand-dot{width:16px;height:16px}
  .envelope-front .brand-name{font-size:10px}
  .envelope-front .return{position:absolute;left:24px;top:44px;font-size:4.5px}

  .envelope-back{left:734px;top:672px;width:431px;height:198px;background:var(--blue)}
  .envelope-back .web{position:absolute;left:0;right:0;top:26px;text-align:center;font-size:5px;color:#e6f0fb;letter-spacing:.06em}
</style>
</head>
<body>
<main class="canvas">

  <section class="sheet letterhead" aria-label="Letterhead">
    <svg class="swoosh" viewBox="0 0 390 540" preserveAspectRatio="none" aria-hidden="true">
      <path d="M200 540 C300 516 370 476 390 376 L390 540 Z" fill="var(--blue)"/>
      <path d="M330 540 C370 516 385 486 390 446 L390 540 Z" fill="var(--red)"/>
      <path d="M200 540 C300 520 366 482 382 396 C372 466 316 516 240 540 Z" fill="#fff" opacity=".35"/>
    </svg>
    <div class="mark-faint"></div>
    <div class="brand"><span class="brand-dot"></span><span class="brand-name">KEYSTONE RIDGE SERVICES</span></div>
    <div class="small contact">
      P (08) 9000 4127<br>
      PO Box 7819 East Perth WA 6892<br>
      callum@keystoneridgeservices.com.au<br>
      keystoneridgeservices.com.au
    </div>
  </section>

  <section class="sheet folder" aria-label="Presentation folder">
    <svg class="swoosh" viewBox="0 0 460 578" preserveAspectRatio="none" aria-hidden="true">
      <path d="M270 0 C370 12 440 50 460 120 L460 0 Z" fill="var(--blue)"/>
      <path d="M390 0 C425 8 452 28 460 58 L460 0 Z" fill="var(--red)"/>
    </svg>
    <div class="brand"><span class="brand-dot"></span><span class="brand-name">KEYSTONE RIDGE SERVICES</span></div>
  </section>

  <section class="sheet card card-front" aria-label="Business card front">
    <svg class="swoosh" viewBox="0 0 203 91" preserveAspectRatio="none" aria-hidden="true">
      <path d="M140 91 C175 84 196 70 203 48 L203 91 Z" fill="var(--blue)"/>
      <path d="M184 91 C194 86 200 78 203 70 L203 91 Z" fill="var(--red)"/>
    </svg>
    <div class="brand"><span class="brand-dot"></span><span class="brand-name">KEYSTONE RIDGE SERVICES</span></div>
    <div class="small details">
      <strong>Callum Brody</strong> · Director<br>
      M 0400 582 913<br>
      callum@keystoneridgeservices.com.au<br>
      EC 20735 · ABN 48 271 502 936
    </div>
  </section>

  <section class="sheet card card-back" aria-label="Business card back">
    <div class="brand"><span class="brand-dot"></span><span class="brand-name">KEYSTONE RIDGE SERVICES</span></div>
    <div class="small web">keystoneridgeservices.com.au</div>
  </section>

  <section class="sheet envelope-front" aria-label="Envelope front">
    <svg class="swoosh" viewBox="0 0 422 203" preserveAspectRatio="none" aria-hidden="true">
      <path d="M270 203 C350 188 408 150 422 94 L422 203 Z" fill="var(--blue)"/>
      <path d="M380 203 C405 191 418 174 422 150 L422 203 Z" fill="var(--red)"/>
    </svg>
    <div class="brand"><span class="brand-dot"></span><span class="brand-name">KEYSTONE RIDGE SERVICES</span></div>
    <div class="small return">PO Box 7819 East Perth WA 6892</div>
  </section>

  <section class="sheet envelope-back" aria-label="Envelope back">
    <svg class="swoosh" viewBox="0 0 431 198" preserveAspectRatio="none" aria-hidden="true">
      <path d="M0 52 L215 198 L431 52 L431 198 L0 198 Z" fill="var(--paper)"/>
      <path d="M0 52 L215 198 L431 52" fill="none" stroke="var(--blue-deep)" stroke-width="1.5"/>
    </svg>
    <div class="small web">keystoneridgeservices.com.au</div>
  </section>

</main>
</body>
</html>
```